Nobody Left the Lantern Burning - Tom Halvery - CD Cover Design Project

Single Cover for CD & Online media e.g. Tunebox Graphics
The first song release from Tom Halvery will be the track 'Nobody Left the Lantern Burning'.
For the release the single requires artwork that is eye catching, seriously professional & meets the requirements of Disc Sprout, Tunebox and also a physical copy on CD.
Track listings for CD will be:
1. Nobody Left the Lantern Burning
2. Nobody Left the Lantern Burning - Instrumental
see details in this link:
http://members.discsprout-example.com/faq.aspx
http://selfmadesound.discsprout-example.com/2009/11/avoid-album-art-atrocities/
http://answers.quorvex-example.com/question/index?qid=20111015141433AAdDTmH
Any advice on this would be greatly appreciated,
I would also like the two logo's I have uploaded to be used,
one is the Tom Halvery logo and the other is for Milbrook & Tandy Records logo (please remove the R and replace with a C for copyright.)
There are four high res photo shopped pictures of Tom Halvery and another zip file of many others, it would be nice to include one of these maybe on the 2nd page or back of the CD. Please don't use them as the front cover.
I imagine an Art Deco illustration but please listen to the track and let it inspire you.
Good Luck
Updates
I don't feel this is what I'm looking for, the design needs to refelct a broken heart without being a picture of a broken heart
Reason: No design has been what we are after so far so the deadline has been extended and the budget increased.

```html
<!DOCTYPE html>
<html lang="en">
<head>
<meta charset="utf-8">
<title>Nobody Left the Lantern Burning – Tom Halvery – Disc Label</title>
<link rel="stylesheet" href="https://fonts.googleapis.com/css2?family=Rubik+Dirt&family=Mulish:wght@400;600&display=swap">
<style>
  :root {
    --page: #ffffff;
    --olive-dark: #3d4a2c;
    --olive: #6f7a3a;
    --moss: #8a8f3c;
    --straw: #d9c46a;
    --cream: #f2e7b8;
    --amber: #c8862f;
    --rust: #a24a1e;
    --ember: #ef6a2c;
    --umber: #3a2b1a;
    --band: rgba(248, 240, 214, 0.78);
    --hub-ring: #d4d5d6;
    --hub-edge: #b9babb;
    --ink-light: #ffffff;
    --ink-dark: #1c1a17;
    --label-red: #7d2534;
  }
  html, body {
    margin: 0;
    padding: 0;
    width: 1200px;
    height: 1200px;
    overflow: hidden;
    background: var(--page);
  }
  .disc-label {
    display: block;
    width: 1200px;
    height: 1200px;
  }
  .title-line {
    font-family: "Rubik Dirt", "Impact", sans-serif;
    fill: var(--ink-light);
    font-size: 52px;
    letter-spacing: 1px;
  }
  .artist-name {
    font-family: "Mulish", "Helvetica", sans-serif;
    font-weight: 400;
    font-size: 44px;
    fill: var(--ink-light);
    letter-spacing: 1px;
  }
  .label-name {
    font-family: "Mulish", "Helvetica", sans-serif;
    font-weight: 600;
    fill: var(--ink-dark);
    font-size: 22px;
  }
  .label-name--record { fill: var(--label-red); font-size: 20px; }
  .title-dots { fill: var(--ink-light); }
</style>
</head>
<body>
<svg class="disc-label" viewBox="0 0 1200 1200" xmlns="http://www.w3.org/2000/svg" role="img" aria-label="CD label for the single Nobody Left the Lantern Burning by Tom Halvery">
  <defs>
    <clipPath id="disc-clip">
      <circle cx="600" cy="600" r="580"/>
    </clipPath>
    <radialGradient id="glow-centre" cx="0.45" cy="0.48" r="0.55">
      <stop offset="0" stop-color="var(--cream)"/>
      <stop offset="0.35" stop-color="var(--straw)"/>
      <stop offset="0.7" stop-color="var(--moss)"/>
      <stop offset="1" stop-color="var(--olive-dark)"/>
    </radialGradient>
    <linearGradient id="warm-base" x1="0" y1="0" x2="0" y2="1">
      <stop offset="0" stop-color="var(--olive-dark)" stop-opacity="0"/>
      <stop offset="0.55" stop-color="var(--amber)" stop-opacity="0.35"/>
      <stop offset="0.85" stop-color="var(--rust)" stop-opacity="0.85"/>
      <stop offset="1" stop-color="var(--umber)" stop-opacity="0.95"/>
    </linearGradient>
    <radialGradient id="dark-corner" cx="0.9" cy="0.15" r="0.5">
      <stop offset="0" stop-color="var(--olive-dark)" stop-opacity="0.7"/>
      <stop offset="1" stop-color="var(--olive-dark)" stop-opacity="0"/>
    </radialGradient>
    <radialGradient id="brush-glow" cx="0.5" cy="0.5" r="0.5">
      <stop offset="0" stop-color="var(--ember)" stop-opacity="0.9"/>
      <stop offset="1" stop-color="var(--ember)" stop-opacity="0"/>
    </radialGradient>
    <radialGradient id="glasses-haze" cx="0.5" cy="0.5" r="0.5">
      <stop offset="0" stop-color="var(--olive)" stop-opacity="0.35"/>
      <stop offset="1" stop-color="var(--olive)" stop-opacity="0"/>
    </radialGradient>
  </defs>

  <g class="disc-artwork" clip-path="url(#disc-clip)">
    <rect class="disc-ground" x="0" y="0" width="1200" height="1200" fill="url(#glow-centre)"/>
    <rect class="disc-warmth" x="0" y="0" width="1200" height="1200" fill="url(#warm-base)"/>
    <rect class="disc-shade" x="0" y="0" width="1200" height="1200" fill="url(#dark-corner)"/>

    <ellipse class="glasses-area" cx="930" cy="240" rx="200" ry="120" fill="url(#glasses-haze)"
      role="img" aria-label="Faint painted pair of spectacles"/>

    <ellipse class="brush-area" cx="620" cy="1000" rx="260" ry="200" fill="url(#brush-glow)"
      role="img" aria-label="Orange painted brush strokes"/>

    <rect class="info-band" x="420" y="452" width="800" height="250" fill="var(--band)"/>

    <g class="artist-mark">
      <rect x="800" y="520" width="22" height="22" fill="var(--ink-dark)"/>
      <text class="label-name" x="800" y="580">Tom</text>
      <text class="label-name" x="800" y="608">Halvery</text>
    </g>

    <g class="record-mark">
      <circle cx="1010" cy="560" r="22" fill="var(--label-red)"/>
      <text class="label-name label-name--record" x="940" y="620">Milbrook &amp; Tandy</text>
      <text class="label-name label-name--record" x="985" y="646">Records</text>
    </g>

    <g class="single-title">
      <text class="title-line" transform="translate(150 255) rotate(30)">Nobody Left</text>
      <text class="title-line" x="70" y="650">the Lantern</text>
      <text class="title-line" transform="translate(150 860) rotate(-22)">Burning</text>
      <g class="title-dots">
        <circle cx="130" cy="360" r="5"/><circle cx="155" cy="400" r="4"/><circle cx="175" cy="435" r="4"/>
        <circle cx="240" cy="690" r="4"/><circle cx="275" cy="700" r="4"/><circle cx="310" cy="712" r="4"/>
        <circle cx="345" cy="722" r="4"/><circle cx="140" cy="770" r="5"/><circle cx="175" cy="765" r="4"/>
      </g>
    </g>

    <text class="artist-name" x="577" y="925">Tom Halvery</text>
  </g>

  <g class="disc-hub">
    <circle cx="600" cy="600" r="157" fill="var(--hub-ring)" stroke="var(--hub-edge)" stroke-width="3"/>
    <circle cx="600" cy="600" r="82" fill="var(--page)" stroke="var(--hub-edge)" stroke-width="3"/>
  </g>
</svg>
</body>
</html>
```